Brochure for medical doctor

I need a brochure for a medical doctor to promote his practice. The brochure should contain his picture, business information (use letterhead from attachment), and the following text:

- Now accepting PI cases on lien!
- Same and next business day appointments available for initial visits, pre-operative clearances, and all other medical needs

- Expedited medical reports sent quickly to your office

Medical

```html
<!DOCTYPE html>
<html lang="en">
<head>
<meta charset="utf-8">
<title>Meadowbrook Medical Center – Patient Lien Flyer</title>
<link rel="stylesheet" href="https://fonts.googleapis.com/css2?family=Montserrat:wght@400;500;600;700;800&display=swap">
<style>
:root{
  --green:#0a8f6a;
  --blue:#1463a8;
  --navy:#155a9c;
  --ink:#1f2a33;
  --paper:#ffffff;
  --mist:#e6f1f8;
  --stage:#ebeef1;
}
*{margin:0;padding:0;box-sizing:border-box}
html,body{width:1200px;height:800px;overflow:hidden;background:var(--stage);font-family:"Montserrat",sans-serif;color:var(--ink)}
.flyer{position:absolute;left:324px;top:10px;width:552px;height:780px;background:var(--paper);overflow:hidden;box-shadow:0 2px 10px rgba(0,0,0,.12)}
.flyer__backdrop{position:absolute;left:0;top:0;width:552px;height:330px;background:linear-gradient(160deg,#f4f8fb 0%,var(--mist) 60%,#d8eaf5 100%)}
.brand{position:absolute;left:30px;top:34px;display:flex;align-items:center;gap:10px}
.brand__dot{width:38px;height:38px;border-radius:50%;background:var(--green)}
.brand__name{font-weight:800;font-size:21px;line-height:1.02;color:var(--green);text-transform:uppercase;letter-spacing:.2px}
.doctor{position:absolute;left:30px;top:106px;width:300px}
.doctor__name{font-weight:800;font-size:21px;color:var(--green);letter-spacing:-.3px;white-space:nowrap}
.doctor__specialty{font-weight:700;font-size:17px;color:var(--ink);margin-top:3px}
.portrait{position:absolute;left:344px;top:18px;width:200px;height:300px}
.portrait__photo{position:absolute;left:12px;top:0;width:176px;height:280px;border-radius:0 0 88px 88px;background:linear-gradient(180deg,#dfe9f1 0%,#f4f6f8 55%,#cfdbe6 100%)}
.band{position:absolute;left:0;top:200px;width:552px;height:250px}
.perks{position:absolute;left:30px;top:262px;width:300px}
.perks__lead{color:#fff;font-weight:600;font-size:11px;margin:0 0 8px 52px}
.perk{display:flex;align-items:center;gap:12px;margin-bottom:8px}
.perk__icon{flex:none;width:40px;height:40px;border-radius:50%;border:2px solid #fff;display:flex;align-items:center;justify-content:center}
.perk__text{color:#fff;font-weight:500;font-size:10.5px;line-height:1.3}
.terms{position:absolute;width:234px}
.terms--release{left:30px;top:450px}
.terms--acknowledge{left:288px;top:388px}
.terms__title{font-weight:800;font-size:12px;line-height:1.25;color:var(--navy);margin-bottom:7px}
.terms__body{font-size:7px;line-height:1.45;text-align:justify;margin-bottom:5px}
.signatures{position:absolute;left:30px;top:678px;width:492px;display:grid;grid-template-columns:1fr 1fr 1fr;column-gap:18px;row-gap:14px}
.sig{border-top:1px dotted #555;padding-top:3px;font-weight:700;font-size:8px}
.footer{position:absolute;left:0;bottom:0;width:552px;height:40px;background:var(--blue);display:flex;align-items:center;justify-content:space-between;padding:0 30px;color:#fff;font-weight:600;font-size:11.5px}
.footer__item{display:flex;align-items:center;gap:7px}
.footer__icon{width:20px;height:20px;border-radius:50%;border:1.5px solid #fff;display:flex;align-items:center;justify-content:center}
</style>
</head>
<body>
<main class="flyer">
  <div class="flyer__backdrop" role="img" aria-label="Faint medical icon pattern on soft blue background"></div>

  <div class="brand">
    <span class="brand__dot"></span>
    <span class="brand__name">Meadowbrook<br>Medical Center</span>
  </div>

  <div class="doctor">
    <h1 class="doctor__name">Dr. Daniel Moreno, MD</h1>
    <p class="doctor__specialty">General Family Medicine</p>
  </div>

  <svg class="band" viewBox="0 0 552 250" aria-hidden="true">
    <defs>
      <linearGradient id="bandFill" x1="0" y1="0" x2="1" y2="0">
        <stop offset="0" stop-color="#0a8f6a"/>
        <stop offset="0.55" stop-color="#137a9a"/>
        <stop offset="1" stop-color="#1463a8"/>
      </linearGradient>
    </defs>
    <polygon points="0,50 552,0 552,120 0,240" fill="url(#bandFill)"/>
  </svg>

  <div class="portrait">
    <svg width="200" height="300" viewBox="0 0 200 300" style="position:absolute;left:0;top:0" aria-hidden="true">
      <path d="M5 200 Q35 300 130 296 Q187 290 198 220" fill="none" stroke="#0a8f6a" stroke-width="14"/>
      <path d="M17 240 Q60 296 139 286" fill="none" stroke="#ffffff" stroke-width="6"/>
      <path d="M174 120 Q205 200 193 236" fill="none" stroke="#1463a8" stroke-width="10"/>
    </svg>
    <div class="portrait__photo" role="img" aria-label="Portrait of the doctor in a white coat with arms crossed"></div>
  </div>

  <section class="perks">
    <p class="perks__lead">Now accepting PI cases on lien!</p>
    <div class="perk">
      <span class="perk__icon"><svg width="18" height="18" viewBox="0 0 24 24" fill="none" stroke="#fff" stroke-width="2"><rect x="4" y="3" width="16" height="18" rx="2"/><circle cx="12" cy="14" r="4"/><path d="M12 12v2l1.5 1"/></svg></span>
      <p class="perk__text">Same and next business day appointments available for initial visits, pre-operative clearances, and all other medical needs</p>
    </div>
    <div class="perk">
      <span class="perk__icon"><svg width="18" height="18" viewBox="0 0 24 24" fill="none" stroke="#fff" stroke-width="2"><rect x="5" y="3" width="14" height="18" rx="1"/><path d="M8 8h8M8 12h8M8 16h5"/></svg></span>
      <p class="perk__text">Expedited medical reports sent quickly to your office</p>
    </div>
  </section>

  <section class="terms terms--release">
    <h2 class="terms__title">Re: Medical Reports<br>and Doctor's Daniel Moreno</h2>
    <p class="terms__body">I authorized the above doctor and or their authorized representatives to furnish my attorney, any attorney or attorneys who subsequently are either associated with the said attorney or substituted in their place, with a full report of my examination, diagnosis, treatment, prognosis, itemized bill of charges incurred, etc, in regard to the accident in which I was involved on ____________, and hold the above doctor free and harmless from any liability in such transfer of information.</p>
    <p class="terms__body">Patient's personal injury claim medical payments are hereby assigned and will be paid directly from the insurance company to Meadowbrook Medical Center.</p>
    <p class="terms__body">Attorney agrees to notify the doctors immediately of the name and contacting information of any attorney substituted in his or her place.</p>
  </section>

  <section class="terms terms--acknowledge">
    <h2 class="terms__title">Acknowledgement of assignment and<br>Daniel Moreno by attorney</h2>
    <p class="terms__body">The undersigned being the attorney of record on his own behalf and on behalf of any other attorney or attorneys who are associated with the undersigned or who are substituted in his stead for the above patient, does hereby acknowledge receipt of a copy of the assignment and lien, and said attorney acknowledges that he/she obligates themselves to the terms of the assignment and lien in consideration for the rendering of medical services to their client by the above doctor and rendering of a report and bill to said attorney. In the event legal action shall be brought in order to enforce this lien, then the prevailing party shall be entitled to reasonable costs and attorney fees in addition to any judgment rendered. A photographic reproduction of this authorization may be used in place of the original. No charges of alterations of the monies billed herein will be accepted unless confirmed in writing by the doctor. Please date, sign and return on copy as soon as possible to the above referenced medical provider of services in order that treatment can continue on the herein contained lien basis.</p>
  </section>

  <section class="signatures">
    <span class="sig">Print Patient Name</span>
    <span class="sig">Date</span>
    <span class="sig">Attorney's Signature</span>
    <span class="sig">Signature Of Patient</span>
    <span class="sig">Signature Of Parent/guardian</span>
    <span class="sig">Date</span>
  </section>

  <footer class="footer">
    <span class="footer__item"><span class="footer__icon"><svg width="10" height="12" viewBox="0 0 10 12"><path d="M5 11S1 6.5 1 4a4 4 0 0 1 8 0c0 2.5-4 7-4 7z" fill="none" stroke="#fff" stroke-width="1.3"/><circle cx="5" cy="4" r="1.3" fill="#fff"/></svg></span>4120 Linden Ave. Bellview, CA, 90000</span>
    <span class="footer__item"><span class="footer__icon"><svg width="10" height="10" viewBox="0 0 24 24"><path d="M6 2l4 5-2 3a12 12 0 0 0 6 6l3-2 5 4-2 4C10 22 2 14 2 4z" fill="#fff"/></svg></span>(555) 014-2210</span>
    <span class="footer__item"><span class="footer__icon"><svg width="10" height="10" viewBox="0 0 24 24"><rect x="5" y="2" width="14" height="8" fill="#fff"/><rect x="2" y="10" width="20" height="8" rx="2" fill="#fff"/><rect x="6" y="15" width="12" height="7" fill="#fff"/></svg></span>(555) 014-2217</span>
  </footer>
</main>
</body>
</html>
```